Kellwood Build, Carpentry Services

Business card for carpentry business in the Sunshine Coast.

Business card layout required using logo provided - provided both PDF copy and AI. Please let me know if you would like a the files for the logo symbol and text by itself.

Business Colours are grey, blue and white. The font colours codes for this design are Blue Hex # 00B4E6 and Hex # 39393B for the gray colour.

FYI font for logo is Gotham Bold.

Preference for a clean and striking layout that is simple and elegant.

Target Market(s)

Young Families, retirees, young couples requiring assistance with small to medium works/renovations on the Sunshine Coast.

Industry/Entity Type

Construction

Contact Information for Business Card

Dean Kellwood
Carpenter
0489305627
dean@kellwoodbuild.com.au
Palmview Bay, Coral Coast
RHPA Licensed Carpenter (In smaller font)

Font styles to use
Sans Serif

Colors

Designer to choose colors to be used in the design.

Requirements
Must have
• Logo provided must appear on the card, preferably on one side of the card by itself with the text on the alternate side
Nice to have
• Text on the other side of card, maybe grey background and white font here but happy for the designer to provide ideas here.
Should not have
• Use of other colours, other than the ones provided - white, grey and blue. Black optional.

```html
<!DOCTYPE html>
<html lang="en">
<head>
<meta charset="UTF-8">
<title>Kellwood Build – Business Card</title>
<link href="https://fonts.googleapis.com/css2?family=Montserrat:wght@700&family=Arimo:wght@400&display=swap" rel="stylesheet">
<style>
  :root {
    --backdrop: #1c1c1d;
    --card-grey: #39393b;
    --brand-blue: #00b4e6;
    --white: #ffffff;
    --soft-white: #e9e9ea;
  }
  * { margin: 0; padding: 0; box-sizing: border-box; }
  html, body { width: 1200px; height: 900px; overflow: hidden; background: var(--backdrop); }
  .canvas {
    width: 1200px; height: 900px;
    display: flex; flex-direction: column; align-items: center; justify-content: center;
    gap: 52px;
  }
  .card {
    width: 640px; height: 366px;
    background: var(--card-grey);
    position: relative;
    overflow: hidden;
  }
  .brand {
    display: flex; align-items: center; gap: 14px;
    font-family: "Montserrat", sans-serif; font-weight: 700;
    color: var(--brand-blue); text-transform: uppercase; letter-spacing: 0.03em;
    white-space: nowrap;
  }
  .brand__square { background: var(--brand-blue); flex: none; }

  .card--front { display: flex; align-items: center; justify-content: center; }
  .card--front .brand { font-size: 44px; }
  .card--front .brand__square { width: 40px; height: 40px; }

  .card--back .brand {
    position: absolute; left: 36px; top: 150px; font-size: 23px; gap: 10px;
  }
  .card--back .brand__square { width: 22px; height: 22px; }
  .divider {
    position: absolute; left: 318px; top: 86px; width: 2px; height: 200px; background: var(--white);
  }
  .contact { position: absolute; left: 344px; top: 92px; font-family: "Arimo", sans-serif; color: var(--soft-white); }
  .contact__name {
    font-family: "Montserrat", sans-serif; font-weight: 700; font-size: 25px;
    color: var(--brand-blue); letter-spacing: 0.02em;
  }
  .contact__role { font-size: 16px; margin-top: 4px; }
  .contact__licence { font-size: 11px; margin-top: 10px; }
  .contact__list { list-style: none; margin-top: 12px; }
  .contact__item { display: flex; align-items: center; gap: 12px; font-size: 15.5px; line-height: 24px; white-space: nowrap; }
  .contact__icon { width: 14px; height: 14px; flex: none; fill: var(--brand-blue); }
</style>
</head>
<body>
<main class="canvas">
  <section class="card card--front" aria-label="Card front">
    <div class="brand"><span class="brand__square"></span>Kellwood Build</div>
  </section>

  <section class="card card--back" aria-label="Card back">
    <div class="brand"><span class="brand__square"></span>Kellwood Build</div>
    <div class="divider"></div>
    <div class="contact">
      <p class="contact__name">Dean Kellwood</p>
      <p class="contact__role">Carpenter</p>
      <p class="contact__licence">RHPA Licensed Carpenter</p>
      <ul class="contact__list">
        <li class="contact__item">
          <svg class="contact__icon" viewBox="0 0 24 24" aria-hidden="true"><path d="M6.6 10.8a15.1 15.1 0 0 0 6.6 6.6l2.2-2.2a1 1 0 0 1 1-.25 11.4 11.4 0 0 0 3.6.57 1 1 0 0 1 1 1V20a1 1 0 0 1-1 1A17 17 0 0 1 3 4a1 1 0 0 1 1-1h3.5a1 1 0 0 1 1 1c0 1.25.2 2.45.57 3.6a1 1 0 0 1-.25 1z"/></svg>
          0489305627
        </li>
        <li class="contact__item">
          <svg class="contact__icon" viewBox="0 0 24 24" aria-hidden="true"><path d="M2 5h20v14H2zm2 2v.5l8 5 8-5V7zm0 2.9V17h16V9.9l-8 5z"/></svg>
          dean@kellwoodbuild.com.au
        </li>
        <li class="contact__item">
          <svg class="contact__icon" viewBox="0 0 24 24" aria-hidden="true"><path d="M12 2a10 10 0 1 0 0 20 10 10 0 0 0 0-20zm0 2c1 0 2.3 2 2.8 5H9.2C9.7 6 11 4 12 4zM4.3 10h3c-.1.7-.1 1.3-.1 2s0 1.3.1 2h-3a8 8 0 0 1 0-4zm4.9 0h5.6a17 17 0 0 1 0 4H9.2a17 17 0 0 1 0-4zm7.5 0h3a8 8 0 0 1 0 4h-3a17 17 0 0 0 0-4zM9.2 15h5.6c-.5 3-1.8 5-2.8 5s-2.3-2-2.8-5z"/></svg>
          www.kellwoodbuild.com.au
        </li>
        <li class="contact__item">
          <svg class="contact__icon" viewBox="0 0 24 24" aria-hidden="true"><path d="M12 2a7 7 0 0 0-7 7c0 5.2 7 13 7 13s7-7.8 7-13a7 7 0 0 0-7-7zm0 9.5A2.5 2.5 0 1 1 12 6.5a2.5 2.5 0 0 1 0 5z"/></svg>
          Palmview Bay, Coral Coast
        </li>
      </ul>
    </div>
  </section>
</main>
</body>
</html>
```